Acai Bowls, Smoothies and Juice Bar Menu

Design a tri fold menu for our Acai bowl, smoothie and juice bar. It should fit in a standard, stand-up brochure holder at our register (POS) stand...

Target Market(s)

Health food lovers, high school kids, discerning eaters who want a healthy alternative meal. people who loves smoothies, fresh juices, Acai bowls.

Industry/Entity Type

Food Service

Requirements
Must have
• All of our information, social, address, etc. Our logo and our slogan: Eat smart, live healthy! Also, if you give us a formatted, titled area for each product: BOWLS, JUICES, SMOOTHIES, TOPPINGS & EXTRAS, we can add in each item as well. NO PRICING. Choose colors based on our new logo.
• I UPLOADED OUR EXISTING MENU SO YOU KNOW WHAT WE ARE WORKING WITH ... BUT OUR NAME IS NOT CUP OF MEADOWS, IT IS NOW TIZZLES CUPS AS YOU SEE IN THE LOGO.
• Sections on the menu should be:
• Acai Bowls
• Juices
• Smoothies
• Toppings and Extras
• Acai Berry benefits
• Social, website (tizzlescups.example)
• slogan: Eat smart, live healthy!
Nice to have
• I would like an area that is the benefits of Acai ... the original menu will give you an idea of some of things that should be on the menu. However like I stated below, we cannot use existing art or slogans, etc from Cup of Meadows.
Should not have
• THIS IS VERY IMPORTANT:
• NOTHING from the existing menus I put into the brief should be used, no slogans, no images, nothing. We are no longer a Cup of Meadows franchise, so nothing from the original menu can be used.

```html
<!DOCTYPE html>
<html lang="en">
<head>
<meta charset="utf-8">
<title>Tizzles Cups Menu</title>
<link rel="stylesheet" href="https://fonts.googleapis.com/css2?family=Kaushan+Script&family=Oswald:wght@400&family=Montserrat:wght@500&display=swap">
<style>
:root{
  --bg:#eeeeee;
  --paper:#f7f7f5;
  --purple:#5f327f;
  --purple-wash:#b9a3c6;
  --orange:#e08a1e;
  --green:#6e9a3c;
  --green-light:#8fbc5a;
  --green-wash:#b8cf9c;
  --peach-wash:#f6d3ad;
  --ink-light:#f1ecf4;
}
*{box-sizing:border-box;margin:0;padding:0}
html,body{width:1200px;height:1028px;overflow:hidden;background:var(--bg)}
.menu{position:absolute;left:67px;top:34px;width:1065px;height:960px;display:flex;box-shadow:0 6px 24px rgba(0,0,0,.12)}
.panel{position:relative;width:355px;height:960px;background:var(--paper);overflow:hidden}
.panel-bowls{background:
  radial-gradient(ellipse 60% 18% at 40% 5%,var(--purple-wash),transparent 70%),
  radial-gradient(ellipse 60% 12% at 30% 98%,var(--purple-wash),transparent 70%),var(--paper)}
.panel-juices{background:
  radial-gradient(ellipse 55% 16% at 45% 4%,var(--peach-wash),transparent 70%),
  radial-gradient(ellipse 60% 20% at 20% 82%,var(--peach-wash),transparent 70%),
  radial-gradient(ellipse 45% 20% at 95% 18%,var(--green-wash),transparent 70%),var(--paper)}
.panel-smoothies{background:
  radial-gradient(ellipse 70% 20% at 60% 6%,var(--green-wash),transparent 70%),
  radial-gradient(ellipse 60% 20% at 20% 25%,var(--green-wash),transparent 70%),var(--paper)}
.script-title{font-family:"Kaushan Script",cursive;text-align:center;line-height:.95}
.panel-bowls .script-title{color:var(--orange);font-size:50px;padding-top:28px}
.panel-juices .script-title{color:var(--green-light);font-size:50px;padding-top:28px}
.panel-smoothies .script-title{color:var(--purple);font-size:44px;padding-top:56px}
.bowl-box{position:absolute;left:18px;right:18px;top:168px;bottom:34px;background:var(--purple);padding:18px 14px 10px 14px;display:flex;flex-direction:column;justify-content:space-between}
.item-name{font-family:"Oswald",sans-serif;font-size:18px;line-height:1.1}
.bowl-box .item-name{color:var(--orange)}
.desc{font-family:"Montserrat",sans-serif;font-size:7px;line-height:1.3;text-transform:uppercase;letter-spacing:.2px;padding-left:8px}
.bowl-box .desc{color:var(--ink-light)}
.toppings-label{display:block;color:var(--orange);margin-top:5px}
.juice-grid{position:absolute;left:14px;right:14px;top:150px;display:grid;grid-template-columns:1fr 1fr;row-gap:8px}
.juice{text-align:center}
.juice.centered{grid-column:1 / span 2;justify-self:center;width:50%}
.juice-photo{width:104px;height:100px;margin:0 auto;border-radius:40% 40% 30% 30%}
.juice .item-name{color:var(--green-light);font-size:17px;margin-top:4px}
.juice .desc{color:var(--orange);font-size:6.5px;padding:0 20px}
.green-box{position:absolute;left:18px;right:18px;background:var(--green);padding:14px 10px;color:var(--ink-light)}
.box-smoothies{top:128px;height:232px}
.box-boost{top:372px;height:144px}
.box-extras{top:528px;height:226px}
.green-box .item-name{color:var(--purple);font-size:17px;margin-top:4px}
.green-box .desc{color:var(--ink-light)}
.box-heading{font-family:"Oswald",sans-serif;font-size:17px;color:var(--purple);margin-bottom:8px}
.plain-list{font-family:"Montserrat",sans-serif;font-size:11px;line-height:1.2;text-transform:uppercase;color:var(--ink-light);list-style:none}
.boost-cols{display:flex;gap:8px}
.boost-cols .plain-list{flex:1}
.tiny{font-size:5.5px;display:block}
</style>
</head>
<body>
<main class="menu">
  <section class="panel panel-bowls">
    <h2 class="script-title">Acai<br>Bowls</h2>
    <div class="bowl-box">
      <div class="item"><h3 class="item-name">North Shore Original</h3><p class="desc">Organic acai, strawberries, bananas, blueberries, 100% apple juice and Berry 7<span class="toppings-label">Toppings:</span>Organic granola (hemp + flax seed), bananas and honey</p></div>
      <div class="item"><h3 class="item-name">Dex's Peanut Butter</h3><p class="desc">Organic acai, strawberries, peanut butter, chocolate almond milk and Berry 7<span class="toppings-label">Toppings:</span>Organic granola (hemp + flax seed), bananas and honey</p></div>
      <div class="item"><h3 class="item-name">Seasider</h3><p class="desc">Organic acai, strawberries, bananas, pineapple, blueberries, unsweetened vanilla almond milk and Berry 7<span class="toppings-label">Toppings:</span>Shredded coconut, fresh strawberries and honey</p></div>
      <div class="item"><h3 class="item-name">Sunset</h3><p class="desc">Pineapple, mango, strawberries, unsweetened coconut milk and Berry 7<span class="toppings-label">Toppings:</span>Organic granola (hemp + flax seed), shredded coconut, fresh kiwi, fresh strawberries and honey</p></div>
      <div class="item"><h3 class="item-name">Leafy Strong</h3><p class="desc">Pineapple, mango, strawberries, unsweetened coconut milk and Berry 7<span class="toppings-label">Toppings:</span>Organic granola (hemp + flax seed), shredded coconut, fresh kiwi, fresh strawberries and honey</p></div>
      <div class="item"><h3 class="item-name">Paradise</h3><p class="desc">Organic pitaya, pineapple, bananas, fresh mint, prickly pear blend and Berry 7<span class="toppings-label">Toppings:</span>Organic granola (hemp + flax seed), shredded coconut, fresh kiwi, fresh strawberries and honey</p></div>
      <div class="item"><h3 class="item-name">Lime-A-Licious</h3><p class="desc">Organic acai, strawberries, pineapple, blueberries, peaches, fresh lime, coconut water and Berry 7<span class="toppings-label">Toppings:</span>Organic granola (hemp + flax seed), shredded coconut, fresh strawberries, fresh blueberries and honey</p></div>
      <div class="item"><h3 class="item-name">Red Zinger</h3><p class="desc">Organic acai, mango, pineapple, blueberries, raspberries, fresh lime, fresh ginger, coconut water and Berry 7<span class="toppings-label">Toppings:</span>Organic granola (hemp + flax seed), dark vanilla chocolate, fresh raspberries and honey</p></div>
    </div>
  </section>

  <section class="panel panel-juices">
    <h2 class="script-title">Fresh<br>&nbsp;&nbsp;Juices</h2>
    <div class="juice-grid">
      <div class="juice"><div class="juice-photo" role="img" aria-label="Glass of green juice with carrots, kale and lemon" style="background:linear-gradient(160deg,#9ccc6a,#f08a3a)"></div><h3 class="item-name">Bulk-N-Ator</h3><p class="desc">Carrot, kale, spinach, parsley, lemon</p></div>
      <div class="juice"><div class="juice-photo" role="img" aria-label="Glass of golden juice with apple, lime and ginger" style="background:linear-gradient(160deg,#f3c14a,#7fae3f)"></div><h3 class="item-name">Root Boost</h3><p class="desc">Carrot, apple, lime, ginger</p></div>
      <div class="juice"><div class="juice-photo" role="img" aria-label="Glass of orange juice with carrots, oranges and apples" style="background:linear-gradient(160deg,#f6b43a,#e4602b)"></div><h3 class="item-name">C-Power</h3><p class="desc">Carrot, orange, apple</p></div>
      <div class="juice"><div class="juice-photo" role="img" aria-label="Glass of orange juice with kiwi, orange and strawberry" style="background:linear-gradient(160deg,#f6b43a,#8aa63a)"></div><h3 class="item-name">Tropicale</h3><p class="desc">Orange, kiwi, strawberry</p></div>
      <div class="juice"><div class="juice-photo" role="img" aria-label="Glass of green juice with cucumber, celery, kale and lemon" style="background:linear-gradient(160deg,#b5d67a,#4f8a2e)"></div><h3 class="item-name">Green Glory</h3><p class="desc">Apple, cucumber, celery, kale, spinach, lemon, parsley</p></div>
      <div class="juice"><div class="juice-photo" role="img" aria-label="Glass of deep red juice with beets and apple" style="background:linear-gradient(160deg,#7a1f3a,#c0392b)"></div><h3 class="item-name">Heart Beet</h3><p class="desc">Apple, lemon, beet</p></div>
      <div class="juice"><div class="juice-photo" role="img" aria-label="Shot glass of wheatgrass beside fresh wheatgrass" style="background:linear-gradient(160deg,#a6d06a,#4d8a2a)"></div><h3 class="item-name">Wheat Grass Shot</h3><p class="desc">Fresh wheatgrass</p></div>
      <div class="juice"><div class="juice-photo" role="img" aria-label="Shot glass of ginger juice with lemon, lime and ginger root" style="background:linear-gradient(160deg,#f3dc6a,#9bb84a)"></div><h3 class="item-name">Ginger Shot</h3><p class="desc">Ginger, lemon, lime</p></div>
      <div class="juice centered"><div class="juice-photo" role="img" aria-label="Glass of orange juice with sliced oranges" style="background:linear-gradient(160deg,#f8b23a,#ee7a1f)"></div><h3 class="item-name">Oranges</h3><p class="desc">Oranges</p></div>
    </div>
  </section>

  <section class="panel panel-smoothies">
    <h2 class="script-title">Smoothies</h2>
    <div class="green-box box-smoothies">
      <h3 class="item-name">Aloha Delight</h3><p class="desc">Mango, pineapple, bananas, avocado, organic yacon, 11 grams of vanilla plant protein, and unsweetened coconut milk</p>
      <h3 class="item-name">Berry Blast</h3><p class="desc">Organic acai, strawberries, bananas, blueberries, 100% apple juice and Berry 7</p>
      <h3 class="item-name">Peanut Butter Blast</h3><p class="desc">Organic acai, bananas, strawberries, natural peanut butter, dark chocolate almond milk and Berry 7</p>
      <h3 class="item-name">Leafy Blast</h3><p class="desc">Organic acai, strawberries, pineapple, blueberries, bananas, fresh kale, fresh spinach, 100% apple juice and Berry 7</p>
      <h3 class="item-name">Purple Rain</h3><p class="desc">Organic acai, pineapple, fresh apple, blueberries, aronia berries, organic purple corn, organic cinnamon, unsweetened coconut milk</p>
    </div>
    <div class="green-box box-boost">
      <h3 class="box-heading">ADD BOOST:</h3>
      <div class="boost-cols">
        <ul class="plain-list"><li>Plat protein boosts<span class="tiny">Made with pea, hemp, rice &amp; chia seeds</span></li><li>Chocolate</li><li>Vanilla</li><li>Green</li><li>Berry 7</li></ul>
        <ul class="plain-list"><li>Fresh kale</li><li>Fresh spinach</li><li>Fresh mint</li><li>Fresh ginger</li><li>Organic pitaya</li><li>Organic acai</li></ul>
      </div>
    </div>
    <div class="green-box box-extras">
      <h3 class="box-heading">EXTRA TOPPINGS:</h3>
      <ul class="plain-list"><li>Organic granola</li><li>Paleo granola</li><li>Shredded coconut</li><li>Honey</li><li>Dark vanilla chocolate</li><li>Fresh strawberries</li><li>Fresh blueberries</li><li>Fresh raspberries</li><li>Fresh kiwi</li><li>Bee pollen</li></ul>
    </div>
  </section>
</main>
</body>
</html>
```